Letterhead for New Orthopaedic Surgery Practice

My husband and I are starting our own practice named RB Spine & Vitality Center. We would like to create a nice simple but high class letterhead that doesn't use too much solid color ink when printing. I like the colors dark blue, gold, yellow. Open to other suggestions. We will need to list him and I both on the top of the letterhead. Here is the important information:
Lucinda Perrow, M.D. - Hand and Upper Extremity Surgery
Abena Quist, M.D. - Hip & Knee Replacement/General Orthopaedic Surgery
Location: 18735 North Harlow Pkwy
Marlow Springs, FL 33490
Phone: 954-218-4650
Fax: 954-582-1346
Email: info@myrbspine.com

The only thing is that the phone and fax numbers will change once we get into our space. I just want to get the design started. I am including several documents which are my previous practice letterhead, my current procedure room letterhead, and our new Logo. The other letterheads are just for examples but please think outside of the box! We would love to see some great designs.

Colors
0054AA
0677BA
7BADD7
CADEEF
E8F1F8
0094D4
00A9DD
6FCCEA
C7EBF8
E9F6FB

Requirements
Must have
• class, elegance, luxury

```html
<!DOCTYPE html>
<html lang="en">
<head>
<meta charset="utf-8">
<title>RB Spine &amp; Vitality Center — Letterhead</title>
<link href="https://fonts.googleapis.com/css2?family=Bebas+Neue&family=Roboto:wght@400&display=swap" rel="stylesheet">
<style>
  :root {
    --navy: #1f3a83;
    --sky: #12b2dc;
    --rule: #3b5aa6;
    --grey-text: #8a8a8a;
    --icon-top: #1b8fd6;
    --icon-bottom: #1c4f98;
    --watermark: #e7eaf3;
    --backdrop: #ececec;
    --paper: #ffffff;
    --edge: #7a7a7a;
  }
  * { margin: 0; padding: 0; box-sizing: border-box; }
  html, body { width: 1200px; height: 1200px; overflow: hidden; }
  body { background: var(--backdrop); position: relative; font-family: 'Roboto', Arial, sans-serif; }

  .sheet {
    position: absolute; left: 193px; top: 30px;
    width: 813px; height: 1140px;
    background: var(--paper);
    border-bottom: 2px solid var(--edge);
    box-shadow: 0 2px 10px rgba(0,0,0,0.08);
  }

  .doctors { position: absolute; left: 0; top: 0; width: 100%; height: 128px; }
  .doctors__divider { position: absolute; left: 406px; top: 0; width: 1px; height: 128px; background: var(--rule); }

  .doctor { position: absolute; top: 27px; }
  .doctor__name {
    font-family: 'Bebas Neue', 'Oswald', sans-serif;
    font-size: 33px; line-height: 32px; letter-spacing: 0.2px;
  }
  .doctor__specialty {
    margin-top: 9px; font-size: 10.8px; color: var(--grey-text); letter-spacing: 0.1px;
  }
  .doctor--left { right: 459px; text-align: right; }
  .doctor--left .doctor__name { color: var(--navy); }
  .doctor--right { left: 461px; text-align: left; }
  .doctor--right .doctor__name { color: var(--sky); }

  .contact-band {
    position: absolute; left: 0; top: 128px; width: 100%; height: 37px;
    border-top: 1px solid var(--rule); border-bottom: 1px solid var(--rule);
  }
  .contact { position: absolute; top: 5px; display: flex; align-items: center; gap: 9px; }
  .contact__icon { width: 22px; height: 22px; flex: none; }
  .contact__text { font-size: 11.6px; line-height: 14px; color: var(--grey-text); }
  .contact--phone { left: 150px; }
  .contact--web { left: 324px; }
  .contact--address { left: 499px; }

  .watermark {
    position: absolute; left: 0; top: 560px; width: 100%;
    display: flex; align-items: center; justify-content: center; gap: 28px;
  }
  .watermark__dot { width: 110px; height: 110px; border-radius: 50%; background: var(--watermark); flex: none; }
  .watermark__name {
    font-family: 'Bebas Neue', 'Oswald', sans-serif;
    font-size: 60px; line-height: 58px; color: var(--watermark);
  }
</style>
</head>
<body>
  <svg width="0" height="0" style="position:absolute">
    <defs>
      <linearGradient id="iconFill" x1="0" y1="0" x2="0" y2="1">
        <stop offset="0" stop-color="#1b8fd6"/>
        <stop offset="1" stop-color="#1c4f98"/>
      </linearGradient>
    </defs>
  </svg>

  <main class="sheet">
    <header class="doctors">
      <div class="doctor doctor--left">
        <div class="doctor__name">Lucinda<br>Perrow, M.D.</div>
        <div class="doctor__specialty">HAND &amp; UPPER EXTREMITY SURGERY</div>
      </div>
      <div class="doctors__divider"></div>
      <div class="doctor doctor--right">
        <div class="doctor__name">Abena<br>Quist, M.D.</div>
        <div class="doctor__specialty">HIP &amp; KNEE REPLACEMENT/GENERAL ORTHOPAEDIC SURGERY</div>
      </div>
    </header>

    <section class="contact-band">
      <div class="contact contact--phone">
        <svg class="contact__icon" viewBox="0 0 22 22">
          <rect width="22" height="22" rx="3" fill="url(#iconFill)"/>
          <path d="M7.2 5.5c.5-.3 1.1-.2 1.4.3l1.2 1.9c.3.5.2 1-.2 1.4l-.8.7c.6 1.3 1.6 2.4 2.9 3l.7-.8c.4-.4 1-.5 1.4-.2l1.9 1.2c.5.3.6 1 .3 1.4l-.7.9c-.6.8-1.7 1-2.6.6-3-1.3-5.3-3.6-6.5-6.6-.4-.9-.1-2 .6-2.6z" fill="#fff"/>
        </svg>
        <div class="contact__text">954 218 4650<br>954 582 1346</div>
      </div>
      <div class="contact contact--web">
        <svg class="contact__icon" viewBox="0 0 22 22">
          <rect width="22" height="22" rx="3" fill="url(#iconFill)"/>
          <path d="M5 11.2 16.5 6l-3.4 11-2.7-3.8-2.9 2.1.8-3.5z" fill="#fff"/>
        </svg>
        <div class="contact__text">info@myrbspine.com<br>www.myrbspine.com</div>
      </div>
      <div class="contact contact--address">
        <svg class="contact__icon" viewBox="0 0 22 22">
          <rect width="22" height="22" rx="3" fill="url(#iconFill)"/>
          <path d="M11 4.5a4.6 4.6 0 0 0-4.6 4.6c0 3.3 4.6 8.4 4.6 8.4s4.6-5.1 4.6-8.4A4.6 4.6 0 0 0 11 4.5z" fill="#fff"/>
          <circle cx="11" cy="9.1" r="1.8" fill="#1c4f98"/>
        </svg>
        <div class="contact__text">18735 North Harlow Pkwy<br>Marlow Springs, FL 33490</div>
      </div>
    </section>

    <div class="watermark" aria-hidden="true">
      <div class="watermark__dot"></div>
      <div class="watermark__name">RB Spine &amp;<br>Vitality Center</div>
    </div>
  </main>
</body>
</html>
```